依頼詳細
PCとスマホデザインの両方納品をいただきますが、
まずはデザインイメージが確認しやすいPCページのみの提案をお願いします。
スマホページは当選者に納品時にお願いしたいと思います。
スマホサイズについて、カンバスサイズは横幅375pxで作成し、2倍の横幅750pxのサイズで書き出ししてください。
(Retinaディスプレイに対応するため)
スマホページ作成時は、メニューが展開した際のデザインもお願いします。
レスポンシブウェブデザインを意識したデザインでお願いします。

■サイトマップ
添付の画面遷移図をご確認ください。

■参考サイト
https://www.hirotoku-sarumi.jp/
https://www.tabuse-seiban.co.jp/

■内容について
主に鋼材の卸売業を行う会社の公式サイトになります。
卸売だけでなく、鋼板を仕入れて希望のサイズに切断、プレスなどの加工も行う会社です。
参考サイトはメインビジュアルが動画になっていますが、今回のサイトデザインでは動画を使用する予定は今のところありません。

■素材写真
画像データについては、フリー素材から流用して
イメージ画像に当て込んでください。
足りない場合は、一旦他のサイトの写真をサンプルとして
入れてください。(サンプルなどの表記をお願いします)
また、購入が必要な写真などを利用した場合、
価格とサイト名を教えてください。

また、Pixoral Imageで定期契約をしていますので、
Pixoral Imageの画像は使用できます。
デザイン時はカンプ画像をお入れいただきますようお願いします。

■ロゴについて
添付のロゴデータを使用してください。

■ワイヤーフレーム
https://mock.velqara.net/view/52817caa-1f3b-4d0e-9a72-6e1b8c37d904-b39f/?fullscreen
コンテンツの構成としてワイヤーフレームを作成しましたが
必ずしもワイヤーフレームの通りではなくて大丈夫です。
TOPページに配置するコンテンツを見ていただき、デザインは
デザイナーの皆様におまかせしたいと思います。

----------------------------------------------------------------------------
【制作物に対するお願い】

■フォントについて
・無料で使えるフォントで作成をお願いします。
・OSに紐づくフォントの使用は控えていただければと思います (ヒラギノなど)

ページ数
1ページ
希望イメージ
シンプル 複雑
単色 カラフル
暗い 明るい
日常 高級
遊び心 厳粛
未来的 伝統的
女性的 男性的
希望する色
ベースカラー:白、青、ポイントカラー:赤
納品ファイル
• 高解像度JPG (.jpg)
• イラストレーター形式 (.ai)
• フォトショップ形式 (.psd)
補足説明
上記のいずれか1つ(アウトラインありとなしの2つ)と高解像度JPGを納品お願いします。
adobe XDでの納品も可能です。
CS5にバージョンを落としたロゴデータです。
ロゴのpngデータも追加しました。

```html
<!DOCTYPE html>
<html lang="ja">
<head>
<meta charset="UTF-8">
<title>北原スチール株式会社</title>
<link href="https://fonts.googleapis.com/css2?family=Noto+Sans+JP:wght@400;500;700;900&family=Montserrat:wght@500;600;700&display=swap" rel="stylesheet">
<style>
:root{
  --red:#d4121c;
  --ink:#2a2a2a;
  --muted:#8a8a8a;
  --line:#d9d9d9;
  --footer:#3a3a3a;
  --white:#ffffff;
  --steel-dark:#4b5560;
  --steel-mid:#8d99a5;
  --steel-light:#cfd6dd;
}
*{margin:0;padding:0;box-sizing:border-box}
html,body{width:1200px;height:3372px;overflow:hidden}
body{font-family:"Noto Sans JP",sans-serif;color:var(--ink);background:var(--white);position:relative}
.abs{position:absolute}
.en{font-family:"Montserrat",sans-serif}
.photo{position:absolute}

/* header */
.site-header{position:absolute;left:0;top:0;width:1200px;height:66px;background:var(--white);z-index:5}
.brand{position:absolute;left:44px;top:22px;display:flex;align-items:center;gap:8px;font-weight:900;font-size:17px;color:var(--red)}
.brand i{width:12px;height:12px;background:var(--red);display:block}
.global-nav{position:absolute;right:170px;top:24px;display:flex;gap:40px;font-size:13px;font-weight:500}
.global-nav a{color:var(--ink);text-decoration:none}
.global-nav a.current{color:var(--red)}
.header-contact{position:absolute;right:0;top:0;width:130px;height:82px;background:var(--red);color:#fff;font-size:12px;display:flex;flex-direction:column;align-items:center;justify-content:center;gap:6px}

/* hero */
.hero-accent{left:0;top:66px;width:300px;height:500px;background:var(--red)}
.hero-photo{left:60px;top:0;width:1140px;height:560px;background:linear-gradient(180deg,#20262d 0%,#4f5a66 35%,#9aa6b2 60%,#6c7784 100%)}
.hero-copy{left:110px;top:360px;color:#fff;font-size:54px;font-weight:900;letter-spacing:.06em}
.hero-copy em{font-style:normal;color:var(--red);font-size:64px}
.hero-lead{left:110px;top:456px;color:#fff;font-size:14px;letter-spacing:.08em}

/* about */
.about-accent{left:0;top:560px;width:80px;height:640px;background:var(--red)}
.about-photo-main{left:0;top:690px;width:540px;height:240px;background:linear-gradient(135deg,#59636d,#b6bec6 50%,#727d88)}
.about-photo-sub{left:420px;top:930px;width:190px;height:170px;background:linear-gradient(160deg,#9aa3ab,#dfe4e8 55%,#7a838c)}
.sec-title{font-size:24px;font-weight:700;letter-spacing:.06em}
.sec-label{font-size:10px;color:var(--red);letter-spacing:.15em;margin-top:6px}
.catch{font-size:16px;font-weight:700;color:var(--red);letter-spacing:.04em}
.body-text{font-size:12px;line-height:2;color:#555;letter-spacing:.04em}
.link-line{width:180px;border-bottom:1px solid var(--ink);font-size:12px;padding-bottom:8px;display:flex;justify-content:space-between}

/* recruit */
.recruit-photo{left:0;top:1230px;width:1200px;height:380px;background:linear-gradient(180deg,#2e353d,#7d8893 50%,#c8cfd6)}
.recruit-card{left:160px;top:1510px;width:820px;height:400px;background:linear-gradient(90deg,#fff 70%,rgba(255,255,255,.85))}
.recruit-person{left:730px;top:1450px;width:270px;height:230px;background:linear-gradient(180deg,#d6dbe0,#eef1f3)}

/* news */
.news-list{left:380px;top:2040px;width:660px}
.news-row{display:flex;gap:40px;border-bottom:1px solid var(--line);padding:12px 0 12px 20px;font-size:12px}
.news-row time{color:var(--muted);width:60px}

/* contact */
.contact-photo{left:0;top:2420px;width:790px;height:520px;background:linear-gradient(135deg,#e9ecef,#b8c0c8 60%,#8b949d)}
.contact-box{left:600px;top:2540px;width:600px;height:400px;background:var(--red);color:#fff;padding:50px 60px}
.contact-box .sec-label{color:#fff}
.tel{display:flex;align-items:center;gap:10px;font-size:30px;font-weight:700;margin-top:24px}
.btn-outline{width:300px;height:52px;border:1px solid #fff;display:flex;align-items:center;justify-content:center;font-size:13px;margin-top:22px}

/* footer */
.site-footer{left:0;top:2940px;width:1200px;height:432px;background:var(--footer);color:#ddd}
.site-footer .brand{color:#fff}
.site-footer .brand i{background:#fff}
.footer-info{left:164px;top:70px;font-size:11px;line-height:1.9;color:#ccc}
.footer-btn{left:164px;top:144px;width:190px;height:40px;border:1px solid #bbb;font-size:11px;display:flex;align-items:center;justify-content:center}
.footer-nav{left:730px;top:54px;display:flex;gap:44px;font-size:11px}
.footer-sub{left:880px;top:168px;display:flex;gap:30px;font-size:10px;color:#aaa}
.copyright{left:0;top:300px;width:1200px;text-align:center;font-size:10px;color:#aaa}
</style>
</head>
<body>

<header class="site-header">
  <div class="brand"><i></i>北原スチール株式会社</div>
  <nav class="global-nav">
    <a class="current en">TOP</a><a>事業内容</a><a>会社情報</a><a>採用情報</a>
  </nav>
  <div class="header-contact">
    <svg width="20" height="14" viewBox="0 0 20 14"><rect x="1" y="1" width="18" height="12" fill="none" stroke="#fff"/><path d="M1 1l9 7 9-7" fill="none" stroke="#fff"/></svg>
    お問い合わせ
  </div>
</header>

<section class="hero">
  <div class="abs hero-accent"></div>
  <div class="photo hero-photo" style="top:66px;height:494px" role="img" aria-label="倉庫に並ぶ鋼板コイルの写真"></div>
  <h1 class="abs hero-copy"><em>鋼</em>で<em>未来</em>を形にする。</h1>
  <p class="abs hero-lead">鋼材の卸売と、一貫した加工技術で、お客様の理想をかたちにします。</p>
</section>

<section class="about">
  <div class="abs about-accent"></div>
  <div class="photo about-photo-main" role="img" aria-label="巻かれた鋼板コイルの写真"></div>
  <div class="photo about-photo-sub" role="img" aria-label="積み重ねた鋼板の写真"></div>
  <div class="abs" style="left:600px;top:690px">
    <h2 class="sec-title">北原スチールについて</h2>
    <p class="sec-label en">ABOUT</p>
  </div>
  <p class="abs catch" style="left:600px;top:770px">テキストが入りますテキストが入ります</p>
  <p class="abs body-text" style="left:600px;top:806px;width:450px">鋼材の仕入れから切断、プレス加工まで一貫して対応しています。長年培った技術と確かな品質で、地域のものづくりを支え続けています。</p>
  <div class="abs link-line" style="left:820px;top:950px"><span>事業内容</span><span>→</span></div>
  <div class="abs link-line" style="left:820px;top:1006px"><span>会社情報</span><span>→</span></div>
</section>

<section class="recruit">
  <div class="photo recruit-photo" role="img" aria-label="工場内に並ぶ鋼材コイルの写真"></div>
  <div class="abs recruit-card"></div>
  <div class="photo recruit-person" role="img" aria-label="作業着姿の社員の写真"></div>
  <div class="abs" style="left:220px;top:1560px">
    <h2 class="sec-title">採用情報</h2>
    <p class="sec-label en">RECRUIT</p>
  </div>
  <p class="abs catch" style="left:220px;top:1630px">テキストが入りますテキストが入ります</p>
  <p class="abs body-text" style="left:220px;top:1666px;width:420px">私たちと一緒に、鋼の可能性を広げる仲間を募集しています。未経験の方も丁寧な研修で一人前の技術者へと成長できます。</p>
  <div class="abs link-line" style="left:220px;top:1846px"><span>詳しくはこちら</span><span>→</span></div>
</section>

<section class="news">
  <div class="abs" style="left:164px;top:2010px">
    <h2 class="sec-title">お知らせ</h2>
    <p class="sec-label en">NEWS</p>
  </div>
  <div class="abs news-list">
    <div class="news-row"><time class="en">2024.00.00</time><span>お知らせが入ります。お知らせが入ります。お知らせが入ります。</span></div>
    <div class="news-row"><time class="en">2024.00.00</time><span>お知らせが入ります。お知らせが入ります。お知らせが入ります。</span></div>
    <div class="news-row"><time class="en">2024.00.00</time><span>お知らせが入ります。お知らせが入ります。お知らせが入ります。</span></div>
    <div class="news-row"><time class="en">2024.00.00</time><span>お知らせが入ります。お知らせが入ります。お知らせが入ります。</span></div>
    <div class="news-row"><time class="en">2024.00.00</time><span>お知らせが入ります。お知らせが入ります。お知らせが入ります。</span></div>
  </div>
</section>

<section class="contact">
  <div class="photo contact-photo" role="img" aria-label="図面を確認する作業員の手元の写真"></div>
  <div class="abs contact-box">
    <h2 class="sec-title">お問い合わせ</h2>
    <p class="sec-label en">CONTACT</p>
    <p style="font-size:12px;margin-top:22px">ご質問やご相談など、お気軽にお問い合わせください。</p>
    <div class="tel en">
      <svg width="26" height="26" viewBox="0 0 24 24"><path d="M6.6 10.8a15 15 0 006.6 6.6l2.2-2.2a1 1 0 011-.25 11.4 11.4 0 003.6.57 1 1 0 011 1V20a1 1 0 01-1 1A17 17 0 013 4a1 1 0 011-1h3.5a1 1 0 011 1 11.4 11.4 0 00.57 3.6 1 1 0 01-.25 1z" fill="#fff"/></svg>
      0250-41-7305
    </div>
    <p style="font-size:11px;margin-top:4px;padding-left:36px">受付時間 平日 8:30〜17:30</p>
    <div class="btn-outline">Webからのお問い合わせ　→</div>
  </div>
</section>

<footer class="abs site-footer">
  <div class="brand" style="left:164px;top:40px">
    <i></i>北原スチール株式会社
  </div>
  <p class="abs footer-info">〒950-0000 新潟県北原市工業団地1-2-3<br>TEL 0250-41-7305<br>FAX 0250-41-7306</p>
  <div class="abs footer-btn">お問い合わせ　→</div>
  <nav class="abs footer-nav"><span class="en">TOP</span><span>事業内容</span><span>会社情報</span><span>採用情報</span></nav>
  <div class="abs footer-sub"><span>プライバシーポリシー</span><span>サイトマップ</span></div>
  <p class="abs copyright en">Copyright © 北原スチール株式会社 All Rights Reserved.</p>
</footer>

</body>
</html>
```